Three Banner Ad Concepts Multiple Sizes For Pixelhive Native Ads Network Campaigns

I would like to see THREE totally different concepts using the content below. Once I approve the THREE DESIGN CONCEPTS I will need them in 5 different sizes for each of the 3 approved concepts.

So technically I am asking for THREE totally different designs in FIVE Sizes. See Sizes below.

I will advertise these banners on zentrix ad display network, vimbly.com as well as pixelhive so please keep these in mind and if you have experience creating these type of ads then this is great.

Headlines:
1. Boost Responses To Your Ads Without Increasing Ad Spend Giving Away Free Smartwatches and Norvicks You Don't Personally Need To Fulfill!

2. Attract More Customers During Tough Times Giving Away Free Vacation & Dining Vouchers That You Don't Need To Pay For!

3. Increase Conversions On Your Website Offering A Free Hotel Stay Or Even A Smart Watch In Exchange For Their Form Submission!

Calls To Actions:
1. Get A Free Sample Package
2. Sign Up For A Free Trial
3. Book A Demo

Native Ads Sizes
Image Size 600x600
Image Size 600x500
Image Size 600x315

Pixelhive (for px ads please take into account the 20% text rule in the image):
For carousel: 1200x1200 pixels
For regular image ads: 1200x628 pixels

Target Market(s)

B2B, Small Business Owners, Entrepreneurs, Marketing Directors, Sales Managers

Industry/Entity Type

Marketing

Requirements
Must have
• Use images from lumarta.com as I have account here
Nice to have
• These designs need to be B2B based....Use images that compliment the TEXT and speak to a BUSINESS OWNER and NOT A CONSUMER!!
Should not have
• DO NOT CREATE AN AD THAT IS B2C based, this is a B2B ad. please check website www.brightlanepromotionhub.biz

```html
<!DOCTYPE html>
<html lang="en">
<head>
<meta charset="utf-8">
<title>Brightlane Promotion Hub – Boost Responses Banner</title>
<link rel="stylesheet" href="https://fonts.googleapis.com/css2?family=Montserrat:wght@500;700;800&display=swap">
<style>
  :root {
    --sky: #29b6f0;
    --sky-deep: #0a8fdc;
    --white: #ffffff;
    --headline-blue: #1768b3;
    --orange: #f7941d;
    --orange-cta: #f99a1c;
    --navy: #1c2b4f;
    --ink: #1f2a3a;
    --logo-blue: #1a5fa8;
  }
  * { box-sizing: border-box; margin: 0; padding: 0; }
  html, body {
    width: 1200px;
    height: 630px;
    overflow: hidden;
    background: var(--white);
  }
  .banner {
    position: relative;
    width: 1200px;
    height: 630px;
    overflow: hidden;
    font-family: "Montserrat", Arial, sans-serif;
    background:
      radial-gradient(ellipse 700px 520px at 760px 230px, #7fdcff 0%, var(--sky) 45%, var(--sky-deep) 100%);
  }
  .backdrop {
    position: absolute;
    inset: 0;
    width: 1200px;
    height: 630px;
  }
  .brand {
    position: absolute;
    left: 0;
    top: 0;
    width: 430px;
    height: 96px;
    background: var(--white);
    clip-path: polygon(0 0, 100% 0, 88% 100%, 0 100%);
    display: flex;
    align-items: center;
    gap: 14px;
    padding-left: 30px;
  }
  .brand-mark {
    width: 30px;
    height: 30px;
    background: var(--logo-blue);
    flex: none;
  }
  .brand-name {
    color: var(--logo-blue);
    font-weight: 700;
    font-size: 19px;
    letter-spacing: 1.5px;
    text-transform: uppercase;
    line-height: 1.15;
    width: 280px;
  }
  .product { position: absolute; }
  .product-earbuds {
    left: 490px;
    top: 0;
    width: 200px;
    height: 310px;
    border-radius: 0 0 40px 40px;
    background: linear-gradient(180deg, #ffffff 0%, #eef1f4 70%, #d9dee4 100%);
  }
  .product-watch {
    left: 790px;
    top: 50px;
    width: 270px;
    height: 370px;
    border-radius: 130px;
    background: radial-gradient(circle at 50% 50%, #3a3f47 0%, #1d2026 55%, #0d0f12 100%);
  }
  .headline {
    position: absolute;
    left: 30px;
    top: 290px;
    color: var(--headline-blue);
    text-transform: uppercase;
    font-size: 50px;
    line-height: 52px;
    letter-spacing: 0.5px;
  }
  .headline-strong { font-weight: 800; display: block; }
  .headline-light { font-weight: 500; display: block; }
  .offer {
    position: absolute;
    left: 416px;
    top: 478px;
    color: var(--ink);
    font-size: 25px;
    line-height: 34px;
    font-weight: 500;
  }
  .offer-lead {
    display: block;
    color: var(--orange);
    font-weight: 800;
    text-transform: uppercase;
    font-size: 26px;
    letter-spacing: 0.5px;
    margin-bottom: 2px;
  }
  .cta {
    position: absolute;
    left: 866px;
    top: 504px;
    width: 290px;
    height: 96px;
    border-radius: 48px;
    background: var(--orange-cta);
    color: var(--navy);
    font-weight: 800;
    font-size: 21px;
    line-height: 28px;
    text-transform: uppercase;
    text-align: center;
    display: flex;
    align-items: center;
    justify-content: center;
    text-decoration: none;
  }
</style>
</head>
<body>
<main class="banner">
  <svg class="backdrop" viewBox="0 0 1200 630" aria-hidden="true">
    <defs>
      <linearGradient id="left-fade" x1="0" y1="0" x2="1" y2="0">
        <stop offset="0" stop-color="#ffffff"/>
        <stop offset="0.55" stop-color="#eaf7fe"/>
        <stop offset="1" stop-color="#ffffff" stop-opacity="0"/>
      </linearGradient>
    </defs>
    <path class="panel-left" d="M0 230 C 200 290, 360 330, 560 420 L 560 630 L 0 630 Z" fill="url(#left-fade)"/>
    <path class="panel-right" d="M560 630 C 760 540, 1000 420, 1200 300 L 1200 630 Z" fill="#ffffff"/>
    <path class="swoosh-line" d="M0 190 C 300 240, 560 380, 860 430 C 980 450, 1090 440, 1200 410" fill="none" stroke="#f7941d" stroke-width="3"/>
  </svg>

  <header class="brand">
    <span class="brand-mark"></span>
    <span class="brand-name">Brightlane Promotion Hub</span>
  </header>

  <div class="product product-earbuds" role="img" aria-label="Photo of white wireless earbuds in an open charging case"></div>
  <div class="product product-watch" role="img" aria-label="Photo of a black round smartwatch showing the time"></div>

  <h1 class="headline">
    <span class="headline-strong">Boost</span>
    <span class="headline-strong">Responses</span>
    <span class="headline-light">To your ads</span>
    <span class="headline-light">without</span>
    <span class="headline-light">increasing</span>
    <span class="headline-light">ad spend</span>
  </h1>

  <p class="offer">
    <span class="offer-lead">Giving away free</span>
    smartwatches and Norvicks<br>
    to your customers
  </p>

  <a class="cta" href="#">Get a free<br>sample package</a>
</main>
</body>
</html>
```